Velvet Paw Hospital Business Card Design

I need a business card designed for my cat only veterinary clinic. I will upload the logo that I would like included on the card. Please include:
Business Name: The Velvet Paw Hospital
Address: 20947 E. 38th St, Scottsdale, AZ 85371
Phone #: 480-555-6143
Website URL: www.velvetpawvets.com
And the Doctors Name: Marisol Brenn, DVM

```html
<!DOCTYPE html>
<html lang="en">
<head>
<meta charset="utf-8">
<title>The Velvet Paw Hospital – Business Card</title>
<link href="https://fonts.googleapis.com/css2?family=Quicksand:wght@400;500;700&display=swap" rel="stylesheet">
<style>
  :root {
    --backdrop: #8a8a8a;
    --card-white: #ffffff;
    --brand-blue: #5a8cc8;
    --name-blue: #4f86c4;
    --ink: #2a2a2a;
    --text-gray: #5a5a5a;
    --accent-pink: #b8306a;
    --mark-dark: #1c1424;
  }
  * { margin: 0; padding: 0; box-sizing: border-box; }
  html, body { width: 1200px; height: 801px; overflow: hidden; }
  body {
    background: var(--backdrop);
    font-family: "Quicksand", sans-serif;
    display: flex;
    align-items: center;
    justify-content: center;
    gap: 40px;
  }
  .card {
    position: relative;
    width: 540px;
    height: 309px;
    border-radius: 3px;
    overflow: hidden;
    box-shadow: 0 10px 24px rgba(0,0,0,0.25);
  }
  /* Front */
  .card-front { background: var(--card-white); }
  .photo-area {
    position: absolute;
    right: 0; top: 0;
    width: 300px; height: 100%;
    background: linear-gradient(90deg, #ffffff 0%, #efe6ea 22%, #c9a5b0 55%, #6e4a5c 100%);
  }
  .brand {
    position: absolute;
    left: 28px; top: 38px;
    display: flex; align-items: center; gap: 12px;
  }
  .brand-dot {
    width: 66px; height: 66px; border-radius: 50%;
    background: var(--mark-dark);
    flex-shrink: 0;
  }
  .brand-name {
    font-weight: 500;
    font-size: 19px;
    line-height: 1.05;
    letter-spacing: 0.5px;
    color: var(--ink);
  }
  .details { position: absolute; left: 30px; top: 134px; }
  .doctor {
    color: var(--name-blue);
    font-weight: 700;
    font-size: 22px;
    margin-bottom: 12px;
  }
  .address {
    color: var(--text-gray);
    font-size: 14px;
    line-height: 1.45;
    margin-bottom: 10px;
  }
  .contact-line {
    display: flex; align-items: center; gap: 8px;
    color: var(--text-gray);
    font-size: 14px;
    line-height: 1.5;
  }
  .contact-line svg { width: 12px; height: 12px; fill: var(--accent-pink); }
  /* Back */
  .card-back {
    background: var(--brand-blue);
    display: flex; align-items: center; justify-content: center;
  }
  .card-back .brand { position: static; }
  .card-back .brand-name { color: #ffffff; font-size: 22px; }
  .card-back .brand-dot { width: 72px; height: 72px; }
</style>
</head>
<body>
  <section class="card card-front">
    <div class="photo-area" role="img" aria-label="Photograph of a long-haired cat resting by a bright window"></div>
    <div class="brand">
      <div class="brand-dot"></div>
      <div class="brand-name">The Velvet Paw<br>Hospital</div>
    </div>
    <div class="details">
      <p class="doctor">Marisol Brenn, DVM</p>
      <p class="address">20947 E. 38th St<br>Scottsdale, AZ 85371</p>
      <p class="contact-line">
        <svg viewBox="0 0 24 24" aria-hidden="true"><path d="M6.6 10.8a15.1 15.1 0 0 0 6.6 6.6l2.2-2.2c.3-.3.7-.4 1-.2 1.1.4 2.3.6 3.6.6.6 0 1 .4 1 1V20c0 .6-.4 1-1 1A17 17 0 0 1 3 4c0-.6.4-1 1-1h3.5c.6 0 1 .4 1 1 0 1.3.2 2.5.6 3.6.1.3 0 .7-.2 1z"/></svg>
        480-555-6143
      </p>
      <p class="contact-line">
        <svg viewBox="0 0 24 24" aria-hidden="true"><circle cx="12" cy="12" r="10"/></svg>
        www.velvetpawvets.com
      </p>
    </div>
  </section>

  <section class="card card-back">
    <div class="brand">
      <div class="brand-dot"></div>
      <div class="brand-name">The Velvet Paw<br>Hospital</div>
    </div>
  </section>
</body>
</html>
```